Tech business card design

We need an amazing business card design for our new business 'Brakka' a marketing tech startup based in Sydney, Australia. We provide an online marketplace for businesses to search and buy advertising media, connect with service providers and learn more about marketing. We wish to communicate 'cool tech', reliability and professionalism and design based around our logo.

Target Market(s)

Business Owners

Contact Information for Business Card

Name
Position
Email Address
Website
Phone Number

Font styles to use
Other font styles liked:
• Avenir & Avenir Next

Colors

Designer to choose colors to be used in the design.

```html
<!DOCTYPE html>
<html lang="en">
<head>
<meta charset="utf-8">
<title>Brakka Business Card</title>
<link href="https://fonts.googleapis.com/css2?family=Nunito+Sans:wght@400;600;800&display=swap" rel="stylesheet">
<style>
  :root {
    --stage: #1c2836;
    --card-blue: #2b2f9c;
    --card-mid: #23308f;
    --card-deep: #1a2a78;
    --glow: #3545b8;
    --silver: #cfd2d8;
    --silver-dark: #a9adb7;
    --ink-light: #ffffff;
    --ink-soft: #d9def5;
    --logo-ink: #2b2f9c;
  }
  * { box-sizing: border-box; margin: 0; padding: 0; }
  html, body {
    width: 1200px; height: 781px; overflow: hidden;
    background: var(--stage);
    font-family: "Nunito Sans", "Avenir Next", Avenir, sans-serif;
  }
  .stage { position: relative; width: 1200px; height: 781px; }

  .card {
    position: absolute;
    border-radius: 18px;
    overflow: hidden;
    background:
      radial-gradient(circle at 0% 0%, rgba(53,69,184,0.55) 0%, rgba(53,69,184,0) 30%),
      radial-gradient(circle at 100% 100%, rgba(53,69,184,0.55) 0%, rgba(53,69,184,0) 30%),
      radial-gradient(ellipse at 50% 45%, var(--card-deep) 0%, var(--card-mid) 55%, var(--card-blue) 100%);
    box-shadow: 0 18px 40px rgba(0,0,0,0.45);
  }

  /* Front: contact side */
  .card-front { left: 150px; top: 137px; width: 310px; height: 507px; }
  .front-header {
    position: absolute; top: 0; left: 0; width: 100%; height: 150px;
    background: var(--silver);
    border-bottom: 10px solid var(--silver-dark);
    display: flex; align-items: center; justify-content: center;
  }
  .front-logo {
    font-size: 44px; font-weight: 800; letter-spacing: -1px;
    color: var(--logo-ink);
  }
  .contact { position: absolute; left: 62px; top: 218px; color: var(--ink-light); }
  .contact-name { font-size: 19px; font-weight: 800; letter-spacing: 0.3px; text-transform: uppercase; }
  .contact-role { font-size: 12px; font-weight: 600; margin-top: 2px; }
  .contact-list { list-style: none; margin-top: 28px; }
  .contact-item {
    display: flex; align-items: center; gap: 10px;
    font-size: 12.5px; font-weight: 400; color: var(--ink-soft);
    margin-bottom: 14px;
  }
  .contact-icon { width: 14px; height: 14px; flex: none; color: var(--ink-light); }
  .contact-at { font-weight: 800; font-size: 15px; color: var(--ink-light); width: 14px; text-align: center; }
  .website {
    position: absolute; right: 30px; bottom: 36px;
    font-size: 13px; color: var(--ink-soft); letter-spacing: 0.3px;
  }

  /* Back: logo side */
  .card-back { left: 540px; top: 235px; width: 507px; height: 310px; }
  .accent-bar {
    position: absolute; height: 10px; width: 70px;
    background: var(--silver); border-radius: 2px;
  }
  .accent-bar-top { top: 36px; left: 36px; }
  .accent-bar-bottom { bottom: 36px; right: 36px; }
  .back-logo {
    position: absolute; top: 50%; left: 50%;
    transform: translate(-50%, -50%);
    font-size: 54px; font-weight: 800; letter-spacing: -1px;
    color: var(--ink-light);
  }
</style>
</head>
<body>
<main class="stage">

  <section class="card card-front" aria-label="Business card front">
    <div class="front-header">
      <div class="front-logo">brakka</div>
    </div>
    <div class="contact">
      <h1 class="contact-name">Liam Carter</h1>
      <p class="contact-role">Founder, Director</p>
      <ul class="contact-list">
        <li class="contact-item">
          <svg class="contact-icon" viewBox="0 0 24 24" aria-hidden="true"><path fill="currentColor" d="M6.6 10.8a15.1 15.1 0 0 0 6.6 6.6l2.2-2.2a1 1 0 0 1 1-.25 11.4 11.4 0 0 0 3.6.57 1 1 0 0 1 1 1V20a1 1 0 0 1-1 1A17 17 0 0 1 3 4a1 1 0 0 1 1-1h3.5a1 1 0 0 1 1 1c0 1.25.2 2.45.57 3.57a1 1 0 0 1-.25 1z"/></svg>
          <span>+61 (0)412 555 208</span>
        </li>
        <li class="contact-item">
          <span class="contact-at" aria-hidden="true">@</span>
          <span>liam@brakkamedia.com.au</span>
        </li>
      </ul>
    </div>
    <p class="website">www.brakkamedia.com.au</p>
  </section>

  <section class="card card-back" aria-label="Business card back">
    <div class="accent-bar accent-bar-top" aria-hidden="true"></div>
    <div class="accent-bar accent-bar-bottom" aria-hidden="true"></div>
    <div class="back-logo">brakka</div>
  </section>

</main>
</body>
</html>
```